VENTURE CAPITAL GROUP BUSINESS CARD DESIGN

Venture Capital Group based in SF looking for a bold business card design. No trendy colour explosion, 3D effects etc. Just "simple" optical effects. Works on your brain, keeps your eye focused and sticks to your mind.
Target Market(s)
Technology startups
Industry/Entity Type
Venture Capital
Contact Information for Business Card
BARNABY WHITLOCK
MANAGING PARTNER
817 FERN ST SAN FRANCISCO, CA 94111
415.555.0143 O
415.555.0167 F
415.555.0192 C
barn@halcyonridgefund.example

```html
<!DOCTYPE html>
<html lang="en">
<head>
<meta charset="utf-8">
<title>Halcyon Ridge Capital Group — Business Card</title>
<link rel="stylesheet" href="https://fonts.googleapis.com/css2?family=Open+Sans:wght@400;600;700;800&display=swap">
<style>
  :root {
    --forest: #0e5a24;
    --forest-deep: #0a4a1c;
    --leaf: #36b43f;
    --silver: #c3c6c9;
    --paper: #ffffff;
    --ink: #0e5a24;
    --stage: #e9ebec;
  }
  * { box-sizing: border-box; margin: 0; padding: 0; }
  html, body { width: 1200px; height: 900px; overflow: hidden; }
  body {
    background: var(--stage);
    font-family: "Open Sans", Arial, sans-serif;
    position: relative;
  }
  .card {
    position: absolute;
    left: 320px;
    width: 560px;
    height: 320px;
    border-radius: 20px;
    overflow: hidden;
    box-shadow: 0 6px 18px rgba(0,0,0,0.15);
  }
  .card-front { top: 110px; background: var(--forest); }
  .card-back { top: 470px; background: var(--paper); }
  .card-art { position: absolute; inset: 0; width: 100%; height: 100%; }

  /* brand name with plain circle */
  .brand { position: absolute; display: flex; flex-direction: column; align-items: center; }
  .brand-dot {
    width: 70px; height: 70px; border-radius: 50%;
    background: #eef0f1; margin-bottom: 12px;
  }
  .brand-name {
    font-weight: 600; text-align: center; line-height: 1.1; letter-spacing: 0.06em;
  }
  .brand-name small { display: block; font-size: 0.38em; letter-spacing: 0.32em; margin-top: 4px; }

  .card-front .brand { left: 0; right: 0; top: 58px; }
  .card-front .brand-name { color: var(--paper); font-size: 28px; }

  .card-back .brand { left: 36px; top: 30px; align-items: flex-start; }
  .card-back .brand-dot { width: 56px; height: 56px; margin-left: 30px; margin-bottom: 10px; background: #e6e8e9; }
  .card-back .brand-name { color: var(--ink); font-size: 20px; text-align: left; }

  .holder {
    position: absolute; right: 40px; top: 72px; text-align: right;
    border-bottom: 1.5px solid var(--forest);
    padding-bottom: 4px; width: 300px;
  }
  .holder-name { font-size: 22px; font-weight: 800; color: var(--forest); letter-spacing: 0.04em; }
  .holder-title { font-size: 10px; font-weight: 600; color: var(--leaf); letter-spacing: 0.08em; }

  .contact {
    position: absolute; left: 40px; top: 168px;
    color: var(--forest); font-size: 11.5px; font-weight: 600;
  }
  .contact-address {
    line-height: 15px; text-transform: uppercase; letter-spacing: 0.02em;
    border-top: 1.5px solid var(--forest); padding-top: 4px; width: 200px; margin-bottom: 6px;
  }
  .contact-list { list-style: none; padding-left: 4px; }
  .contact-list li { display: flex; align-items: center; height: 17px; gap: 10px; }
  .contact-list svg { width: 11px; height: 11px; fill: var(--leaf); flex: none; }
</style>
</head>
<body>

<section class="card card-front" aria-label="Card front">
  <svg class="card-art" viewBox="0 0 560 320" preserveAspectRatio="none" aria-hidden="true">
    <polygon points="0,262 180,262 200,250 560,206 560,218 212,262 205,320 0,320" fill="var(--silver)"/>
    <polygon points="200,250 560,206 560,218 212,262" fill="var(--leaf)"/>
  </svg>
  <div class="brand">
    <span class="brand-dot"></span>
    <p class="brand-name">HALCYON RIDGE<small>CAPITAL GROUP</small></p>
  </div>
</section>

<section class="card card-back" aria-label="Card back">
  <svg class="card-art" viewBox="0 0 560 320" preserveAspectRatio="none" aria-hidden="true">
    <polygon points="0,302 405,262 414,276 0,316" fill="var(--leaf)"/>
    <polygon points="430,246 560,232 560,320 404,320 414,276" fill="var(--forest)"/>
  </svg>

  <div class="brand">
    <span class="brand-dot"></span>
    <p class="brand-name">HALCYON RIDGE<small>CAPITAL GROUP</small></p>
  </div>

  <div class="holder">
    <p class="holder-name">BARNABY WHITLOCK</p>
    <p class="holder-title">MANAGING PARTNER</p>
  </div>

  <div class="contact">
    <p class="contact-address">817 Fern St San<br>Francisco, CA 94111</p>
    <ul class="contact-list">
      <li>
        <svg viewBox="0 0 24 24" aria-label="Office"><path d="M6.6 10.8a15 15 0 0 0 6.6 6.6l2.2-2.2a1 1 0 0 1 1-.25 11.4 11.4 0 0 0 3.6.57 1 1 0 0 1 1 1V20a1 1 0 0 1-1 1A17 17 0 0 1 3 4a1 1 0 0 1 1-1h3.5a1 1 0 0 1 1 1c0 1.25.2 2.45.57 3.57a1 1 0 0 1-.25 1z"/></svg>
        415.555.0143
      </li>
      <li>
        <svg viewBox="0 0 24 24" aria-label="Fax"><path d="M6 3h9l3 3v4H6zM4 11h16a2 2 0 0 1 2 2v6h-4v2H6v-2H2v-6a2 2 0 0 1 2-2zm4 6v2h8v-2z"/></svg>
        415.555.0167
      </li>
      <li>
        <svg viewBox="0 0 24 24" aria-label="Mobile"><path d="M7 1h10a2 2 0 0 1 2 2v18a2 2 0 0 1-2 2H7a2 2 0 0 1-2-2V3a2 2 0 0 1 2-2zm0 3v14h10V4z"/></svg>
        415.555.0192
      </li>
      <li>
        <svg viewBox="0 0 24 24" aria-label="Email"><path d="M2 5h20v14H2zm2 2v.5l8 5 8-5V7zm0 2.9V17h16V9.9l-8 5z"/></svg>
        barn@halcyonridgefund.example
      </li>
    </ul>
  </div>
</section>

</body>
</html>
```